Wine Label Design

A wine label for 750ml bottles. Same label for different varieties with the variety / region / vintage to be updated as required.
Brand: Beyond the Ridge
Product Use: Front and Back label suitable for a 750 ml bottle (preferably Burgundy bottles)
Design Brief: Beyond the Ridge is a small winery that produces limited amounts of hand crafted wines that are aimed at the mid to top end of the market and requires a label befitting the work that goes into the creation of the wine. In terms of style i don't have any preconceptions and am open to a broad range of design suggestions at the same level of existing premium brands or innovative brands.
Must Have for Front label
Front Label
Beyond the Ridge
2013
Grampians
Shiraz
750ML (should be in smaller text)
Alc. 14% by Vol. (should be in smaller text)
Must Have for Back Label
Beyond the Ridge
2013
Grampians
Shiraz
www.beyondtheridge.com.au (should be in smaller text)
Product of Australia
Alc.14% by Vol. (should be in smaller text)
Contains preservative 220(should be in smaller text)
Below are some guides for dimensions:
The Front Label Size can be between
100 - 120 mm (Width) x 70 - 85 mm (Height)
The back label size can be between
90 mm (Width) x 70 - 85 mm (Height)
Target Market(s)
Medium to top end of the wine market who require the label to be a reflection of the wine.
Industry/Entity Type
Product
Colors
Designer to choose colors to be used in the design.
Look and feel

```html
<!DOCTYPE html>
<html lang="en">
<head>
<meta charset="utf-8">
<title>Beyond the Ridge – Grampians Shiraz Label</title>
<link rel="stylesheet" href="https://fonts.googleapis.com/css2?family=Federant&display=swap">
<style>
  :root {
    --page: #ffffff;
    --label: #ecdcc3;
    --ornament-light: #b9ab96;
    --ornament-dark: #6e6455;
    --ink: #111111;
    --halo: #ffffff;
    --shade: rgba(0, 0, 0, 0.45);
  }
  html, body {
    margin: 0;
    padding: 0;
    overflow: hidden;
    background: var(--page);
  }
  .canvas {
    position: relative;
    width: 1200px;
    height: 900px;
    overflow: hidden;
    background: var(--page);
  }
  .label-shape {
    position: absolute;
    left: 0;
    top: 0;
  }
  .ornament {
    position: absolute;
    background: linear-gradient(180deg, var(--ornament-light), var(--ornament-dark) 50%, var(--ornament-light));
    opacity: 0.55;
    border-radius: 4px;
  }
  .ornament--top    { left: 355px; top: 151px; width: 507px; height: 82px; }
  .ornament--bottom { left: 355px; top: 728px; width: 507px; height: 94px; }
  .ornament--left   { left: 277px; top: 165px; width: 70px; height: 665px;
                      background: linear-gradient(90deg, var(--ornament-light), var(--ornament-dark) 50%, var(--ornament-light)); }
  .ornament--right  { left: 868px; top: 165px; width: 66px; height: 665px;
                      background: linear-gradient(90deg, var(--ornament-light), var(--ornament-dark) 50%, var(--ornament-light)); }
  .label-text {
    position: absolute;
    left: 300px;
    width: 600px;
    text-align: center;
    margin: 0;
    font-family: "Federant", serif;
    color: var(--ink);
    line-height: 1;
    white-space: nowrap;
    text-shadow:
      -2px -2px 0 var(--halo), 2px -2px 0 var(--halo),
      -2px 2px 0 var(--halo), 2px 2px 0 var(--halo),
      0 -2px 0 var(--halo), 0 2px 0 var(--halo),
      -2px 0 0 var(--halo), 2px 0 0 var(--halo),
      5px 5px 4px var(--shade);
  }
  .brand-name { top: 262px; font-size: 64px; letter-spacing: 1px; }
  .vintage    { top: 372px; font-size: 56px; letter-spacing: 3px; }
  .region     { top: 448px; font-size: 74px; letter-spacing: 2px; }
  .variety    { top: 540px; font-size: 74px; letter-spacing: 2px; }
  .volume     { top: 636px; font-size: 26px; }
  .alcohol    { top: 672px; font-size: 28px; letter-spacing: 1px; }
</style>
</head>
<body>
<main class="canvas">
  <svg class="label-shape" width="1200" height="900" viewBox="0 0 1200 900" aria-hidden="true">
    <rect x="318" y="115" width="582" height="762" rx="16" fill="var(--label)"/>
    <rect x="271" y="151" width="670" height="693" rx="18" fill="var(--label)"/>
  </svg>

  <div class="ornament ornament--top" role="img" aria-label="Art nouveau scroll border along the top"></div>
  <div class="ornament ornament--bottom" role="img" aria-label="Art nouveau scroll border along the bottom"></div>
  <div class="ornament ornament--left" role="img" aria-label="Vertical scroll ornament down the left edge"></div>
  <div class="ornament ornament--right" role="img" aria-label="Vertical scroll ornament down the right edge"></div>

  <h1 class="label-text brand-name">Beyond the Ridge</h1>
  <p class="label-text vintage">2013</p>
  <p class="label-text region">GRAMPIANS</p>
  <p class="label-text variety">SHIRAZ</p>
  <p class="label-text volume">750ML</p>
  <p class="label-text alcohol">Alc. 14% by Vol</p>
</main>
</body>
</html>
```